Larkwell Pharmacy opening

We want to have a double sided 5.5"x8.5" flyer for a new Pharmacy opening in a well known strip mall in the neighborhood and we are planning to mail it to neighbors homes.

Want to put the outside pharmacy picture on the main side of the flyer and a coupon with 25% off towards an OTC product on the back in addition to the info below (preferably in a sort of bulletin points not a list (something like the 2 examples attached).

Colors to be red like the exterior sign and blue like the interior wall paint:

Front side should have:
Larkwell pharmacy
Your locally owned and operated pharmacy around the corner.
317-4821 Pendry rd.
Ashcombe ridge plaza
T. 604 927 5583 (call or text)
F. 604-927-5587

Free prescription delivery
Text us for refills
Specialized compounding
Customized compression stockings

The back side should have:

Do you forget taking your medications! We offer multiple compliance packaging options at no additional cost.
Had shingles before or worried to have it? travelling soon? check our vaccinations options!
Suffering side effects? We are experienced to check your medications interactions & different coverage options.
Hard time monitoring your blood pressure? Trying to stop smoking? we can always help.

FEELING BETTER STARTS HERE

```html
<!DOCTYPE html>
<html lang="en">
<head>
<meta charset="utf-8">
<title>Larkwell Pharmacy Opening Flyer</title>
<link href="https://fonts.googleapis.com/css2?family=Exo+2:ital,wght@0,500;0,600;0,700;1,600;1,700;1,800&family=Caveat:wght@600&display=swap" rel="stylesheet">
<style>
:root{
  --red:#e31e24;
  --red-dark:#b5121b;
  --navy:#2b3559;
  --navy-soft:#434c74;
  --panel:#f1f2f5;
  --page:#e6e7e9;
  --white:#ffffff;
}
*{margin:0;padding:0;box-sizing:border-box}
html,body{width:1200px;height:923px;overflow:hidden;background:var(--page)}
body{position:relative;font-family:"Exo 2",sans-serif}
.flyer{position:absolute;top:102px;width:468px;height:720px;background:var(--white);overflow:hidden}
.flyer--front{left:118px}
.flyer--back{left:614px}

/* front */
.storefront-photo{position:absolute;left:0;top:0;width:468px;height:310px;
  background:linear-gradient(180deg,#6b6461 0%,#8d847c 35%,#9aa3a8 62%,#6e7378 100%)}
.brand-band{position:absolute;left:43px;top:242px;width:383px;height:114px;background:var(--red);border-radius:26px 0 0 0}
.brand-band::after{content:"";position:absolute;left:0;bottom:0;width:100%;height:12px;background:var(--red-dark)}
.brand-name{position:absolute;left:16px;top:24px;color:var(--white);font-family:Arial,Helvetica,sans-serif;font-weight:700;font-size:31px;line-height:36px;letter-spacing:.5px}
.brand-circle{position:absolute;left:280px;top:234px;width:128px;height:128px;border-radius:50%;background:var(--red);border:8px solid var(--white)}
.tagline{position:absolute;left:0;top:368px;width:468px;text-align:center;color:var(--navy);font-weight:600;font-size:35px;line-height:36px;letter-spacing:-.3px}
.services{position:absolute;left:54px;top:502px;width:388px;height:128px}
.services .v-rule{position:absolute;left:177px;top:0;width:1px;height:128px;background:var(--navy)}
.services .h-rule{position:absolute;left:0;top:72px;width:388px;height:1px;background:var(--navy)}
.service{position:absolute;display:flex;gap:6px;align-items:flex-start}
.service svg{flex:none;margin-top:4px}
.service-title{color:var(--red);font-weight:700;font-size:19px;line-height:19px}
.service-sub{color:var(--red);font-style:italic;font-weight:600;font-size:14px;line-height:17px}
.contact-bar{position:absolute;left:0;top:651px;width:468px;height:69px;background:var(--navy);color:var(--white);text-align:center;font-weight:600;font-size:16px;line-height:22px;padding-top:13px}
.contact-bar svg{vertical-align:-3px;margin:0 2px}

/* back */
.shelf-photo{position:absolute;left:0;top:170px;width:468px;height:420px;opacity:.35;
  background:linear-gradient(90deg,#c9d3d8 0%,#eef0f2 30%,#eef0f2 70%,#c5d0c9 100%)}
.back-heading{position:absolute;left:0;top:28px;width:468px;text-align:center;color:var(--red);font-style:italic;font-weight:800;font-size:29px;line-height:33px}
.checklist-panel{position:absolute;left:61px;top:102px;width:345px;height:549px;background:var(--panel);border-radius:22px 22px 0 0;opacity:.92}
.compliance-note{position:absolute;left:61px;top:112px;width:345px;text-align:center;color:var(--navy);font-style:italic;font-weight:700;font-size:16.5px;line-height:22px;text-transform:uppercase}
.ribbon{position:absolute;display:flex;align-items:center;gap:12px;padding-left:46px;font-weight:600;font-size:20px;line-height:24px}
.ribbon--red{left:46px;width:376px;background:linear-gradient(90deg,var(--red-dark),var(--red) 20%,#f0575c 55%,var(--red) 90%);color:var(--white);border-radius:10px 0 0 10px}
.ribbon--navy{left:46px;width:376px;background:linear-gradient(90deg,var(--navy),var(--navy-soft) 40%,#6b7397 70%,var(--navy));color:var(--white);border-radius:10px 0 0 10px}
.ribbon--light{left:67px;width:335px;padding-left:25px;background:linear-gradient(90deg,#e9eaef,#ffffff 50%,#e4e6ec);color:var(--navy)}
.coverage-note{position:absolute;left:61px;top:576px;width:345px;text-align:center;color:var(--red);font-style:italic;font-weight:700;font-size:15px;line-height:21px}
.slogan-bar{position:absolute;left:0;top:651px;width:468px;height:69px;background:var(--navy);text-align:center}
.slogan{display:block;padding-top:12px;color:var(--white);font-family:"Caveat",cursive;font-size:33px;line-height:36px}
.slogan-bar svg{position:absolute;left:170px;top:48px}
</style>
</head>
<body>

<section class="flyer flyer--front">
  <div class="storefront-photo" role="img" aria-label="Photo of the pharmacy storefront in the strip mall with its red exterior sign"></div>
  <div class="brand-band">
    <div class="brand-name">LARKWELL<br>PHARMACY</div>
  </div>
  <div class="brand-circle"></div>
  <h1 class="tagline">Your locally owned<br>and operated pharmacy<br>around the corner.</h1>

  <div class="services">
    <div class="v-rule"></div>
    <div class="h-rule"></div>
    <div class="service" style="left:8px;top:18px">
      <svg width="32" height="32" viewBox="0 0 32 32"><circle cx="16" cy="16" r="13.5" fill="none" stroke="#2b3559" stroke-width="3"/><path d="M9 16l6 6L28 6" fill="none" stroke="#2b3559" stroke-width="3.5" stroke-linecap="round" stroke-linejoin="round"/></svg>
      <div><div class="service-title">FREE</div><div class="service-sub">prescription delivery</div></div>
    </div>
    <div class="service" style="left:200px;top:16px">
      <svg width="32" height="32" viewBox="0 0 32 32"><circle cx="16" cy="16" r="13.5" fill="none" stroke="#2b3559" stroke-width="3"/><path d="M9 16l6 6L28 6" fill="none" stroke="#2b3559" stroke-width="3.5" stroke-linecap="round" stroke-linejoin="round"/></svg>
      <div><div class="service-title">SPECIALIZED</div><div class="service-sub">compounding</div></div>
    </div>
    <div class="service" style="left:8px;top:87px">
      <svg width="32" height="32" viewBox="0 0 32 32"><circle cx="16" cy="16" r="13.5" fill="none" stroke="#2b3559" stroke-width="3"/><path d="M9 16l6 6L28 6" fill="none" stroke="#2b3559" stroke-width="3.5" stroke-linecap="round" stroke-linejoin="round"/></svg>
      <div><div class="service-title">TEXT US</div><div class="service-sub">for refills</div></div>
    </div>
    <div class="service" style="left:198px;top:87px">
      <svg width="32" height="32" viewBox="0 0 32 32"><circle cx="16" cy="16" r="13.5" fill="none" stroke="#2b3559" stroke-width="3"/><path d="M9 16l6 6L28 6" fill="none" stroke="#2b3559" stroke-width="3.5" stroke-linecap="round" stroke-linejoin="round"/></svg>
      <div><div class="service-title">CUSTOMIZED</div><div class="service-sub">compression stockings</div></div>
    </div>
  </div>

  <footer class="contact-bar">
    317-4821 Pendry rd. Ashcombe ridge plaza<br>
    (Call or Text)
    <svg width="12" height="18" viewBox="0 0 12 18"><rect x="1" y="1" width="10" height="16" rx="2" fill="none" stroke="#fff" stroke-width="1.6"/><line x1="4.5" y1="14" x2="7.5" y2="14" stroke="#fff" stroke-width="1.4"/></svg>604 927 5583
    <svg width="18" height="16" viewBox="0 0 18 16"><rect x="4" y="1" width="10" height="5" fill="none" stroke="#fff" stroke-width="1.5"/><rect x="1" y="6" width="16" height="7" rx="1.5" fill="#fff"/><rect x="4" y="11" width="10" height="4" fill="#2b3559" stroke="#fff" stroke-width="1.2"/></svg>
    &nbsp;604-927-5587
  </footer>
</section>

<section class="flyer flyer--back">
  <div class="shelf-photo" role="img" aria-label="Faint photo of pharmacy shelves stocked with products"></div>
  <h2 class="back-heading">Do you forget taking your<br>medications!</h2>
  <div class="checklist-panel"></div>
  <p class="compliance-note">We offer multiple compliance<br>packaging options at no<br>additional cost.</p>

  <div class="ribbon ribbon--red" style="top:182px;height:59px">
    <svg width="34" height="34" viewBox="0 0 32 32"><circle cx="16" cy="16" r="13.5" fill="none" stroke="#fff" stroke-width="2.6"/><path d="M9 16l6 6L28 6" fill="none" stroke="#fff" stroke-width="3.2" stroke-linecap="round" stroke-linejoin="round"/></svg>
    <span>Had shingles before or<br>worried to have it?</span>
  </div>
  <div class="ribbon ribbon--light" style="top:242px;height:49px">
    <svg width="34" height="34" viewBox="0 0 32 32"><circle cx="16" cy="16" r="13.5" fill="none" stroke="#2b3559" stroke-width="2.6"/><path d="M9 16l6 6L28 6" fill="none" stroke="#2b3559" stroke-width="3.2" stroke-linecap="round" stroke-linejoin="round"/></svg>
    <span>Travelling soon?</span>
  </div>
  <div class="ribbon ribbon--navy" style="top:292px;height:59px">
    <svg width="34" height="34" viewBox="0 0 32 32"><circle cx="16" cy="16" r="13.5" fill="none" stroke="#fff" stroke-width="2.6"/><path d="M9 16l6 6L28 6" fill="none" stroke="#fff" stroke-width="3.2" stroke-linecap="round" stroke-linejoin="round"/></svg>
    <span>check our vaccinations<br>options!</span>
  </div>
  <div class="ribbon ribbon--light" style="top:352px;height:49px">
    <svg width="34" height="34" viewBox="0 0 32 32"><circle cx="16" cy="16" r="13.5" fill="none" stroke="#2b3559" stroke-width="2.6"/><path d="M9 16l6 6L28 6" fill="none" stroke="#2b3559" stroke-width="3.2" stroke-linecap="round" stroke-linejoin="round"/></svg>
    <span>Suffering side effects?</span>
  </div>
  <div class="ribbon ribbon--red" style="top:402px;height:59px">
    <svg width="34" height="34" viewBox="0 0 32 32"><circle cx="16" cy="16" r="13.5" fill="none" stroke="#fff" stroke-width="2.6"/><path d="M9 16l6 6L28 6" fill="none" stroke="#fff" stroke-width="3.2" stroke-linecap="round" stroke-linejoin="round"/></svg>
    <span>Hard time monitoring<br>your blood pressure?</span>
  </div>
  <div class="ribbon ribbon--light" style="top:462px;height:49px">
    <svg width="34" height="34" viewBox="0 0 32 32"><circle cx="16" cy="16" r="13.5" fill="none" stroke="#2b3559" stroke-width="2.6"/><path d="M9 16l6 6L28 6" fill="none" stroke="#2b3559" stroke-width="3.2" stroke-linecap="round" stroke-linejoin="round"/></svg>
    <span>Trying to stop smoking?</span>
  </div>
  <div class="ribbon ribbon--navy" style="top:512px;height:59px">
    <svg width="34" height="34" viewBox="0 0 32 32"><circle cx="16" cy="16" r="13.5" fill="none" stroke="#fff" stroke-width="2.6"/><path d="M9 16l6 6L28 6" fill="none" stroke="#fff" stroke-width="3.2" stroke-linecap="round" stroke-linejoin="round"/></svg>
    <span>We can always help.</span>
  </div>

  <p class="coverage-note">We are experienced to check your<br>medications interactions &amp; different<br>coverage options.</p>

  <footer class="slogan-bar">
    <span class="slogan">Feeling Better Starts Here</span>
    <svg width="190" height="10" viewBox="0 0 190 10"><path d="M2 8 Q95 0 188 4" fill="none" stroke="#e31e24" stroke-width="2.2" stroke-linecap="round"/></svg>
  </footer>
</section>

</body>
</html>
```